Cartwell - custom section required

Hi, I am preparing a new cartwell site (not yet active).

I want to add a section to a theme that will need to be built from liquid or HTLM or any way that works. This section will be part of the home page. This section will be for information purposes only. The section would help with explain about an outsole, my idea would to be exactly like a premium tyre shop advertises. see link. https://www.vandoro.com/tyres/en-au/car/catalogue/product/falcon-gtx
I have attached my mock up of how the section could look. I am looking for someone to code this section with the interactivity like the tyre site. For example: 1) see the sliders how the come across when you scroll down, with our different properties customised. 2) The image windows with the different angles being nicely interactive ti show largewr image when hovering over. 3) If we could do like they did when you press on the different part of the tyre (for our site it would be the outsole) how it lights up the areas and talks about the properties of that area. So our outsole different parts would light up with different explanations.

This section is a quirky idea but will only really work if it is interactive and very professional. It would be great if the content could be modified without too much difficulty. The section could be different to my mock up, creative ideas that contribute to the feel of this section are welcome.

The design must be compatible with Cartwell so I can just easily drop the code in to create the section.

Target Market(s)

Trendy people

Industry/Entity Type

Fashion

Coding

Coded - Design and coding required

Number of Pages Required

1 page

Requirements
Must have
• Must have responsiveness and animated as described.
Nice to have
• If the branding could be included it would be great.

```html
<!DOCTYPE html>
<html lang="en">
<head>
<meta charset="utf-8">
<title>Vibecrew – Performance Pro Outsole</title>
<link href="https://fonts.googleapis.com/css2?family=Poppins:wght@400;500;600&family=Libre+Baskerville:wght@700&display=swap" rel="stylesheet">
<style>
:root{
  --ink:#111111;
  --text:#1c1c1c;
  --muted:#555555;
  --line:#d9d9d9;
  --bar:#3a3a3a;
  --bar-empty:#9a9a9a;
  --sole-light:#d6d0c6;
  --sole-dark:#bdb5a9;
  --render-light:#cfcfcf;
  --render-dark:#9c9c9c;
  --accent:#e02a1d;
  --footer:#121212;
  --white:#ffffff;
}
*{box-sizing:border-box;margin:0;padding:0}
html,body{width:1200px;height:2388px;overflow:hidden;background:var(--white)}
body{position:relative;font-family:'Poppins',sans-serif;color:var(--text)}
.abs{position:absolute}

/* header */
.site-header{position:absolute;left:0;top:0;width:1200px;height:75px;border-bottom:1px solid var(--line)}
.brand{position:absolute;left:105px;top:16px;font-weight:600;font-size:30px;letter-spacing:1px;color:var(--ink);display:flex;align-items:center;gap:8px}
.brand-dot{width:10px;height:10px;border-radius:50%;background:var(--ink)}
.main-nav{position:absolute;top:28px;left:442px;display:flex;gap:25px;font-size:14px;font-weight:500;color:var(--ink)}
.header-icons{position:absolute;left:1047px;top:27px;display:flex;gap:12px}

/* gallery */
.thumb{position:absolute;left:100px;width:113px;height:118px;border:1px solid #ececec;display:flex;align-items:center;justify-content:center}
.thumb .ph{width:86px;height:86px;border-radius:8px;background:linear-gradient(160deg,var(--sole-light),var(--sole-dark))}
.main-view{left:255px;top:111px;width:301px;height:377px;border-radius:140px/180px;background:radial-gradient(ellipse at 50% 40%,var(--sole-light),var(--sole-dark))}

/* product info */
.product-title{left:665px;top:168px;font-family:'Libre Baskerville',serif;font-weight:700;font-size:25.5px;line-height:31px;color:var(--ink);white-space:nowrap}
.fit-btn{left:666px;top:251px;width:330px;height:44px;border-radius:22px;background:var(--ink);color:var(--white);font-size:14px;font-weight:600;display:flex;align-items:center;justify-content:center}
.size-label{left:666px;top:308px;font-size:14px;font-weight:500;color:var(--ink)}
.size-picker{left:666px;top:339px;width:330px;height:44px;border:1px solid #bdbdbd;border-radius:22px;display:flex;align-items:center;padding-left:29px;font-size:14px;color:#777}
.size-picker span{display:inline-block;text-align:center}

/* uses */
.uses{left:100px;top:526px;display:flex}
.use{display:flex;flex-direction:column;align-items:center;font-size:14px;font-weight:500;color:var(--ink)}
.use .ico{width:48px;height:48px;border-radius:50%;background:#e6e6e6;margin-bottom:16px}

/* description */
.section-title{left:99px;top:643px;font-size:26px;font-weight:500;color:var(--ink)}
.section-lead{left:100px;top:683px;width:480px;font-size:16px;line-height:20px;color:var(--ink)}
.section-body{left:100px;top:733px;width:478px;font-size:12.8px;line-height:23px;color:var(--muted);text-align:justify;letter-spacing:-0.1px}

/* ratings */
.ratings{left:100px;top:882px;width:468px}
.rating{display:flex;align-items:center;height:29.8px}
.rating-label{width:82px;font-size:11.5px;font-weight:500;color:var(--ink)}
.rating-track{display:flex;gap:4px;align-items:center}
.seg{width:35px;height:1px;background:var(--bar-empty)}
.seg.on{background:var(--bar);height:3px}

/* hotspots */
.hotspot-view{left:130px;top:1160px;width:356px;height:457px;border-radius:160px/200px;background:radial-gradient(ellipse at 50% 40%,var(--sole-light),var(--sole-dark))}
.hotspot{position:absolute;width:22px;height:22px;border-radius:50%;background:var(--accent);margin:-11px 0 0 -11px}
.hotspot::before,.hotspot::after{content:"";position:absolute;background:var(--white);left:50%;top:50%}
.hotspot::before{width:10px;height:2px;margin:-1px 0 0 -5px}
.hotspot::after{width:2px;height:10px;margin:-5px 0 0 -1px}
.hotspot-tip{left:383px;top:1245px;width:187px;height:43px;background:var(--accent);border:2px solid #a8140a;color:var(--white);font-size:11.5px;font-weight:600;display:flex;align-items:center;justify-content:center}
.tip-close{left:561px;top:1237px;width:16px;height:16px}

/* finish */
.finish-copy{left:100px;top:1704px;width:477px;font-size:15.2px;line-height:30px;color:#444;text-align:justify;text-align-last:right;letter-spacing:-0.1px}
.render{position:absolute;top:1858px;height:112px;border-radius:18px;background:linear-gradient(180deg,var(--render-light),var(--render-dark))}

/* footer */
.site-footer{position:absolute;left:0;top:2054px;width:1200px;height:334px;background:var(--footer);color:var(--white)}
.footer-brand{left:100px;top:66px;font-size:44px;font-weight:600;letter-spacing:2px;display:flex;align-items:center;gap:10px}
.footer-brand .brand-dot{background:var(--white);width:14px;height:14px}
.social{left:134px;top:146px;display:flex;gap:7px}
.social span{width:40px;height:40px;border:1.5px solid var(--white);border-radius:50%}
.fcol{top:58px}
.fcol h4{font-size:15px;font-weight:600;margin-bottom:8px}
.fcol li{list-style:none;font-size:13.5px;line-height:29px}
.contact li{display:flex;gap:6px;align-items:flex-start;line-height:17px;margin-bottom:15px}
.footer-rule{left:100px;top:236px;width:1000px;height:1px;background:#555}
.copyright{left:0;top:258px;width:1200px;text-align:center;font-size:13.5px}
.legal{left:251px;top:296px;font-size:13.5px}
.legal span{position:absolute;white-space:nowrap;top:0}
</style>
</head>
<body>

<header class="site-header">
  <div class="brand"><span class="brand-dot"></span>VIBECREW</div>
  <nav class="main-nav">
    <span>COMPANY</span><span>TYRES CATALOGUE</span><span>TECH &amp; KNOWLEDGE</span><span>TIPS</span><span>PROMOTIONS</span>
  </nav>
  <div class="header-icons">
    <svg width="20" height="20" viewBox="0 0 20 20"><rect x="1" y="4" width="18" height="12" fill="none" stroke="#111" stroke-width="2"/><path d="M1 4l9 7 9-7" fill="none" stroke="#111" stroke-width="2"/></svg>
    <svg width="20" height="20" viewBox="0 0 20 20"><circle cx="10" cy="10" r="9" fill="none" stroke="#111" stroke-width="1.5"/><circle cx="10" cy="8" r="3" fill="#111"/><path d="M4.5 16c1.5-3 9.5-3 11 0" fill="#111"/></svg>
  </div>
</header>

<div class="thumb" style="top:111px"><div class="ph" role="img" aria-label="Outsole pair, bottom view thumbnail"></div></div>
<div class="thumb" style="top:243px"><div class="ph" role="img" aria-label="Heel with wing detail thumbnail"></div></div>
<div class="thumb" style="top:374px"><div class="ph" role="img" aria-label="Outsole side view thumbnail"></div></div>
<div class="abs main-view" role="img" aria-label="Performance Pro outsole pair, bottom view"></div>

<h1 class="abs product-title">VIBECREW'S<br>PERFORMANCE PRO OUTSOLE</h1>
<div class="abs fit-btn">FIT YOUR SHOES</div>
<div class="abs size-label">SIZE</div>
<div class="abs size-picker">
  <span style="width:20px">6</span><span style="width:63px">7</span><span style="width:20px">8</span><span style="width:60px">9</span><span style="width:30px">10</span><span style="width:64px">11</span><span style="width:30px">12</span>
</div>

<div class="abs uses">
  <div class="use" style="width:96px"><span class="ico" role="img" aria-label="All weather icon"></span>ALL WEATHER</div>
  <div class="use" style="width:96px;margin-left:24px"><span class="ico" role="img" aria-label="Glamping icon"></span>GLAMPING</div>
  <div class="use" style="width:96px;margin-left:12px"><span class="ico" role="img" aria-label="Clubbing icon"></span>CLUBBING</div>
  <div class="use" style="width:96px;margin-left:10px"><span class="ico" role="img" aria-label="Festivals icon"></span>FESTIVALS</div>
</div>

<h2 class="abs section-title">Performance Pro Outsole</h2>
<p class="abs section-lead">All weather is welcome. Designed for rugged seasons and unexpected kneesup.</p>
<p class="abs section-body">Vibecrew's Performance Pro is a high performance outsole that features an asymmetrical tread pattern and tread rigidity which ensures the best grip on wet surfaces, and outstanding handling performance on grassed areas. Dynamic Response technology optimizes dance precision for optimum grooves, from city clubs to wet field days</p>

<div class="abs ratings">
  <div class="rating"><span class="rating-label">DRY</span><div class="rating-track"><i class="seg on"></i><i class="seg on"></i><i class="seg on"></i><i class="seg on"></i><i class="seg on"></i><i class="seg on"></i><i class="seg on"></i><i class="seg on"></i><i class="seg" style="width:74px"></i></div></div>
  <div class="rating"><span class="rating-label">WET</span><div class="rating-track"><i class="seg on"></i><i class="seg on"></i><i class="seg on"></i><i class="seg on"></i><i class="seg on"></i><i class="seg on"></i><i class="seg on"></i><i class="seg on"></i><i class="seg on"></i><i class="seg on"></i></div></div>
  <div class="rating"><span class="rating-label">SNOW</span><div class="rating-track"><i class="seg on"></i><i class="seg on"></i><i class="seg on"></i><i class="seg on"></i><i class="seg on"></i><i class="seg on"></i><i class="seg on"></i><i class="seg on"></i><i class="seg on"></i><i class="seg"></i></div></div>
  <div class="rating"><span class="rating-label">COMFORT</span><div class="rating-track"><i class="seg on"></i><i class="seg on"></i><i class="seg on"></i><i class="seg on"></i><i class="seg on"></i><i class="seg on"></i><i class="seg on"></i><i class="seg on"></i><i class="seg on"></i><i class="seg"></i></div></div>
  <div class="rating"><span class="rating-label">OFF-ROAD</span><div class="rating-track"><i class="seg on"></i><i class="seg on"></i><i class="seg on"></i><i class="seg on"></i><i class="seg on"></i><i class="seg on"></i><i class="seg on"></i><i class="seg on"></i><i class="seg" style="width:74px"></i></div></div>
  <div class="rating"><span class="rating-label">MILEAGE</span><div class="rating-track"><i class="seg on"></i><i class="seg on"></i><i class="seg on"></i><i class="seg on"></i><i class="seg on"></i><i class="seg on"></i><i class="seg on"></i><i class="seg on"></i><i class="seg on"></i><i class="seg"></i></div></div>
  <div class="rating"><span class="rating-label">SPORT</span><div class="rating-track"><i class="seg on"></i><i class="seg on"></i><i class="seg on"></i><i class="seg on"></i><i class="seg on"></i><i class="seg on"></i><i class="seg on"></i><i class="seg on"></i><i class="seg on"></i><i class="seg"></i></div></div>
</div>

<div class="abs hotspot-view" role="img" aria-label="Interactive outsole pair with feature hotspots"></div>
<span class="hotspot" style="left:210px;top:1167px"></span>
<span class="hotspot" style="left:458px;top:1218px"></span>
<span class="hotspot" style="left:142px;top:1388px"></span>
<span class="hotspot" style="left:458px;top:1441px"></span>
<span class="hotspot" style="left:173px;top:1582px"></span>
<div class="abs hotspot-tip">RAPID WATER EXPULSION IN</div>
<svg class="abs tip-close" viewBox="0 0 16 16"><circle cx="8" cy="8" r="8" fill="#111"/><path d="M5 5l6 6M11 5l-6 6" stroke="#fff" stroke-width="1.5"/></svg>

<p class="abs finish-copy">Premium design for an appealing finish to your multipurpose boots. The Performance Pro outsole has a unique high contrast side view with a velvet touch. The Branding&nbsp; adds a stylish finish for a boot that looks as good as it performs</p>
<div class="render" style="left:107px;width:204px" role="img" aria-label="Heel render with wing detail"></div>
<div class="render" style="left:360px;width:205px" role="img" aria-label="Outsole side view render"></div>

<footer class="site-footer">
  <div class="abs footer-brand"><span class="brand-dot"></span>VIBECREW</div>
  <div class="abs social">
    <span role="img" aria-label="Social link"></span><span role="img" aria-label="Social link"></span><span role="img" aria-label="Social link"></span><span role="img" aria-label="Social link"></span>
  </div>
  <div class="abs fcol" style="left:465px"><h4>QUICK LINKS</h4><ul><li>About Vibecrew</li><li>Tech &amp; Knowledge</li><li>Tips</li><li>Promotions</li></ul></div>
  <div class="abs fcol" style="left:697px"><h4>ABOUT US</h4><ul><li>Why Vibecrew</li><li>Contact Us</li><li>Company Information</li></ul></div>
  <div class="abs fcol contact" style="left:953px"><h4>CONTACT INFO</h4><ul>
    <li><svg width="12" height="15" viewBox="0 0 12 15"><path d="M6 0a6 6 0 0 1 6 6c0 4-6 9-6 9S0 10 0 6a6 6 0 0 1 6-6z" fill="#fff"/><circle cx="6" cy="6" r="2.2" fill="#121212"/></svg><span>58 Larkfield Lane<br>Brookvale 20931</span></li>
    <li><svg width="14" height="14" viewBox="0 0 14 14"><path d="M3 1l2.5 3-1.5 1.5c1 2 2.5 3.5 4.5 4.5L10 8.5l3 2.5-1.5 2.5C6 13 1 8 0.5 2.5z" fill="none" stroke="#fff" stroke-width="1.3"/></svg><span>+1 555-014-2270</span></li>
    <li><svg width="15" height="11" viewBox="0 0 15 11"><rect width="15" height="11" fill="#fff"/><path d="M0 0l7.5 6L15 0" fill="none" stroke="#121212" stroke-width="1.2"/></svg><span>info@vibecrew.com</span></li>
  </ul></div>
  <div class="abs footer-rule"></div>
  <div class="abs copyright">©Copyright ©2022 VIBECREW. All Rights Reserved.</div>
  <div class="abs legal">
    <span style="left:0">LEGAL INFORMATION</span><span style="left:153px">TERMS OF TRADE</span><span style="left:289px">NEWS</span><span style="left:357px">PRIVACY POLICY</span><span style="left:481px">COOKIE POLICY</span><span style="left:602px">WORK WITH US</span>
  </div>
</footer>

</body>
</html>
```